Beacon Advisory Website

I currently have a website www.beaconadvisoryinc.example. We are a IT Consulting Company. Our website will pretty much tell out our services. I am looking to enhance my website and make it look more professional. Looking for very classy and Contemporary look and design for my website.

Industry/Entity Type

It Company

```html
<!DOCTYPE html>
<html lang="en">
<head>
<meta charset="utf-8">
<title>Beacon Advisory</title>
<link href="https://fonts.googleapis.com/css2?family=Signika:wght@400;600;700&family=Open+Sans:wght@400;600;700&display=swap" rel="stylesheet">
<style>
:root{
  --navy:#34465c;
  --brand:#1a5b96;
  --sky:#0a9bd8;
  --sky-dark:#0a86bd;
  --ink:#222a33;
  --text:#5b6168;
  --muted:#8a9096;
  --grey:#ececec;
  --orange:#f05a28;
  --gold:#e6b422;
  --footer:#262626;
  --white:#fff;
}
*{box-sizing:border-box;margin:0;padding:0}
html,body{width:1200px;height:3629px;overflow:hidden}
body{position:relative;font-family:"Open Sans",sans-serif;color:var(--text);background:var(--white)}
.abs{position:absolute}
h1,h2,h3,h4,.heading{font-family:"Signika",sans-serif}

/* top bar */
.topbar{left:0;top:0;width:1200px;height:48px;background:var(--navy);color:#c9d3de;font-size:13px}
.topbar .social{left:84px;top:16px;display:flex;gap:22px}
.topbar .social span{width:15px;height:15px;border-radius:50%;border:2px solid #a9b6c4;display:block}
.topbar .contact{right:52px;top:15px;display:flex;gap:40px;letter-spacing:.5px}
.topbar .contact b{font-weight:400;display:flex;align-items:center;gap:8px}

/* header */
.header{left:0;top:48px;width:1200px;height:90px;background:var(--white)}
.brand{left:50px;top:22px;display:flex;align-items:center;gap:12px}
.brand .mark{width:44px;height:44px;background:var(--brand)}
.brand .name{font-family:"Signika",sans-serif;font-weight:700;font-size:26px;color:var(--brand);line-height:1}
.nav{right:44px;top:0;display:flex;gap:42px;height:90px;align-items:center;font-size:13px;font-weight:600;color:var(--ink);letter-spacing:.3px}
.nav a{color:inherit;text-decoration:none;position:relative;height:90px;display:flex;align-items:center}
.nav a.active::after{content:"";position:absolute;left:-6px;right:-6px;bottom:0;height:5px;background:var(--brand)}

/* hero */
.hero{left:0;top:138px;width:1200px;height:498px;background:linear-gradient(90deg,#e9ecef 0%,#dfe2e5 40%,#c9ccd0 62%,#4a4a4c 78%,#d4d7db 100%)}
.hero h1{left:48px;top:160px;font-size:38px;font-weight:700;color:var(--brand);letter-spacing:1px}
.hero p{left:48px;top:214px;width:580px;font-size:14px;line-height:20px;color:#1d2228}
.btn-outline{display:flex;align-items:center;gap:12px;border:2px solid var(--ink);border-radius:4px;background:var(--white);color:var(--ink);font-size:16px;padding:0 18px;height:49px}
.hero .btn-outline{left:48px;top:290px;width:202px}

/* about + services */
.about{left:0;top:636px;width:433px;height:438px;background:var(--sky);color:var(--white)}
.about h2{left:60px;top:40px;font-size:34px;font-weight:400;letter-spacing:1px}
.about .rule{left:60px;top:88px;width:90px;height:3px;background:var(--white)}
.about p{left:60px;top:110px;width:340px;font-size:14px;line-height:22px}
.about .btn{left:60px;top:347px;width:153px;height:53px;border:1px solid #bfe6f6;border-radius:3px;display:flex;align-items:center;gap:14px;padding-left:22px;font-size:16px}
.services{left:433px;top:636px;width:767px;height:438px;background:var(--grey)}
.service{width:330px;display:flex;gap:18px}
.service .ico{width:48px;height:48px;flex:none}
.service h3{font-size:18px;font-weight:600;color:var(--ink);margin-bottom:6px}
.service p{font-size:13px;line-height:20px;color:#4e545a}

/* section titles */
.section-title{width:1200px;left:0;text-align:center;font-size:40px;font-weight:600;color:var(--ink)}

/* solutions */
.solution{width:342px}
.solution .photo{height:189px;width:342px}
.solution h3{margin-top:18px;font-size:25px;font-weight:400;color:var(--ink)}
.solution p{margin-top:6px;font-size:13px;line-height:18px;text-align:justify}
.btn-gold{margin-top:18px;width:98px;height:38px;border:2px solid var(--gold);display:flex;align-items:center;justify-content:center;font-size:14px;color:var(--ink)}
.divider{left:48px;top:1643px;width:1104px;height:1px;background:#d9d9d9}

/* testimonial */
.quote{left:576px;top:1780px;width:48px;height:48px;border:2px solid var(--orange);border-radius:50%;display:flex;align-items:center;justify-content:center;color:var(--orange);font-family:Georgia,serif;font-size:30px;font-weight:700;line-height:1}
.testimonial-text{left:110px;top:1850px;width:980px;text-align:center;font-size:14px;line-height:30px;font-style:italic;color:#6f9c9c}
.by{left:0;width:1200px;top:1960px;text-align:center;font-size:11px;color:var(--muted)}
.author{left:0;width:1200px;top:1980px;text-align:center;font-size:13px;font-weight:700;color:var(--ink)}
.hex{width:52px;height:58px;clip-path:polygon(50% 0,100% 25%,100% 75%,50% 100%,0 75%,0 25%)}

/* call band */
.callband{left:48px;top:2195px;width:1104px;height:95px;background:var(--sky);border-radius:6px;color:var(--white)}
.callband .item{top:22px;display:flex;align-items:center;gap:20px}
.callband small{font-size:16px;line-height:24px;color:#d8f0fb;display:block}
.callband .val{font-size:22px}
.callband .or{left:528px;top:23px;width:48px;height:48px;border-radius:50%;background:var(--brand);display:flex;align-items:center;justify-content:center;font-size:13px;font-weight:700}
.callband .split{left:551px;top:0;width:2px;height:95px;background:#57bde8}

/* news */
.news{left:0;top:2290px;width:1200px;height:488px;background:var(--grey)}
.news-card{top:140px;height:266px;display:flex}
.news-card .body{width:278px;height:190px;margin-top:38px;background:var(--white);padding:26px 26px}
.news-card h4{font-size:19px;font-weight:400;color:var(--sky-dark);margin-bottom:14px}
.news-card p{font-size:13px;line-height:22px;color:var(--muted)}
.news-card .more{margin-top:16px;font-size:13px;color:var(--ink)}
.news-card .photo{width:254px;height:266px;position:relative}
.news-card .date{position:absolute;left:0;top:0;width:65px;height:64px;background:var(--orange);color:var(--white);font-size:11px;font-weight:700;text-align:center;line-height:15px;padding-top:18px}

/* consulting hero */
.cta{left:0;top:2778px;width:1200px;height:452px;background:linear-gradient(180deg,#dfe6ec 0%,#b9c6d0 55%,#59636b 100%)}
.cta h2{left:48px;top:80px;font-size:36px;font-weight:700;color:var(--sky);letter-spacing:1px}
.cta p{left:48px;top:138px;font-size:17px;font-weight:700;color:#141a20}
.cta .btn-outline{left:52px;top:196px;width:202px;background:transparent;color:var(--white);border-color:var(--white)}

/* newsletter */
.footer{left:0;top:3230px;width:1200px;height:399px;background:var(--footer);color:var(--white)}
.newsletter{left:48px;top:3098px;width:1104px;height:210px;background:var(--sky);border-radius:6px;text-align:center;color:var(--white)}
.newsletter h2{margin-top:24px;font-size:34px;font-weight:600;letter-spacing:1px}
.newsletter .sub{font-size:16px;font-weight:700;margin-top:2px}
.newsletter form{position:absolute;left:258px;top:122px;display:flex}
.newsletter .field{width:470px;height:52px;background:var(--white);color:#888;font-size:16px;display:flex;align-items:center;padding-left:18px}
.newsletter .submit{width:120px;height:52px;background:var(--brand);font-size:16px;display:flex;align-items:center;justify-content:center}

.footer .brand{left:0;width:1200px;top:156px;justify-content:center}
.footer .brand .name{color:var(--white)}
.footer .brand .mark{background:var(--white)}
.footer .links{left:0;width:1200px;top:240px;text-align:center;font-size:15px;letter-spacing:.5px}
.footer .copy{left:0;width:1200px;top:270px;text-align:center;font-size:15px}
.footer .social{left:0;width:1200px;top:326px;display:flex;justify-content:center;gap:16px}
.footer .social span{width:30px;height:30px;background:var(--white);transform:rotate(45deg);display:block;margin:0 4px}
</style>
</head>
<body>

<div class="abs topbar">
  <div class="abs social"><span></span><span></span><span></span></div>
  <div class="abs contact">
    <b><svg width="14" height="11" viewBox="0 0 14 11"><rect x="1" y="1" width="12" height="9" fill="none" stroke="#a9b6c4" stroke-width="1.5"/><path d="M1 1l6 5 6-5" fill="none" stroke="#a9b6c4" stroke-width="1.5"/></svg>HELLO@BEACONADVISORY.EXAMPLE</b>
    <b><svg width="9" height="15" viewBox="0 0 9 15"><rect x="1" y="1" width="7" height="13" rx="1.5" fill="none" stroke="#a9b6c4" stroke-width="1.5"/></svg>555-010-2040</b>
  </div>
</div>

<header class="abs header">
  <div class="abs brand"><span class="mark"></span><span class="name">BEACON ADVISORY</span></div>
  <nav class="abs nav">
    <a class="active">COMPANY</a><a>SERVICES</a><a>SOLUTIONS</a><a>RESOURCES</a><a>CAREER</a><a>CONTACT US</a>
  </nav>
</header>

<section class="abs hero" role="img" aria-label="Photo of a businessman in a suit using a tablet in a bright office">
  <h1 class="abs">BOOST UP YOUR LOCAL BUSINESS</h1>
  <p class="abs">Lorem Ipsum is simply dummy text of the printing and typesetting industry. Lorem Ipsum has been the industry's standard dummy text ever since the 1500s.</p>
  <div class="abs btn-outline">Start Your Project <svg width="12" height="16" viewBox="0 0 12 16"><path d="M2 2l7 6-7 6" fill="none" stroke="currentColor" stroke-width="3"/></svg></div>
</section>

<section class="abs about">
  <h2 class="abs">BEACON ADVISORY</h2>
  <div class="abs rule"></div>
  <p class="abs">Lorem Ipsum is simply dummy text of the printing and typesetting industry. Lorem Ipsum has been the industry's standard dummy text ever since the 1500s, when an unknown printer took a galley&nbsp; text of the printing and typesetting industry. Lorem Ipsum has been the industry's standard dummy text ever since the 1500s, when an unknown printer took a galley...</p>
  <div class="abs btn">Read More <svg width="12" height="16" viewBox="0 0 12 16"><path d="M2 2l7 6-7 6" fill="none" stroke="#fff" stroke-width="3"/></svg></div>
</section>

<section class="abs services">
  <div class="abs service" style="left:27px;top:30px">
    <svg class="ico" viewBox="0 0 48 48"><circle cx="24" cy="24" r="22" fill="none" stroke="#1a4f86" stroke-width="2.5"/><circle cx="24" cy="24" r="10" fill="none" stroke="#1a4f86" stroke-width="2.5"/><path d="M12 14l24 20" stroke="#1a4f86" stroke-width="2.5"/></svg>
    <div><h3>Technology</h3><p>Company that offers design and build services for you from initial sketches to the final production.</p></div>
  </div>
  <div class="abs service" style="left:431px;top:30px">
    <svg class="ico" viewBox="0 0 48 48"><circle cx="24" cy="24" r="23" fill="#1a4f86"/><rect x="14" y="17" width="20" height="14" fill="none" stroke="#fff" stroke-width="2.5"/><path d="M10 20v8M38 20v8" stroke="#fff" stroke-width="3"/></svg>
    <div><h3>Business</h3><p>Company that offers design and build services for you from initial sketches to the final production.</p></div>
  </div>
  <div class="abs service" style="left:27px;top:175px">
    <svg class="ico" viewBox="0 0 48 48"><circle cx="24" cy="24" r="23" fill="#1a4f86"/><rect x="13" y="14" width="10" height="8" fill="#fff"/><rect x="25" y="26" width="10" height="8" fill="#fff"/><path d="M18 22v8h7M30 26v-8h-7" fill="none" stroke="#fff" stroke-width="2"/></svg>
    <div><h3>Enterprise Integration</h3><p>Company that offers design and build services for you from initial sketches to the final production.</p></div>
  </div>
  <div class="abs service" style="left:431px;top:175px">
    <svg class="ico" viewBox="0 0 48 48"><circle cx="24" cy="24" r="22" fill="none" stroke="#1a4f86" stroke-width="2.5"/><rect x="13" y="15" width="22" height="15" fill="none" stroke="#1a4f86" stroke-width="2.5"/><path d="M20 35h8" stroke="#1a4f86" stroke-width="2.5"/></svg>
    <div><h3>IT Consulting</h3><p>Company that offers design and build services for you from initial sketches to the final production.</p></div>
  </div>
  <div class="abs service" style="left:27px;top:325px">
    <svg class="ico" viewBox="0 0 48 48"><circle cx="24" cy="24" r="22" fill="none" stroke="#1a4f86" stroke-width="2.5"/><rect x="16" y="12" width="16" height="24" rx="2" fill="none" stroke="#1a4f86" stroke-width="2.5"/><path d="M20 20h8M20 25h8" stroke="#1a4f86" stroke-width="2"/></svg>
    <div><h3>Application Developement</h3><p>Company that offers design and build services for you from initial sketches to the final production.</p></div>
  </div>
  <div class="abs service" style="left:431px;top:325px">
    <svg class="ico" viewBox="0 0 48 48"><circle cx="24" cy="24" r="23" fill="#1a4f86"/><rect x="13" y="14" width="22" height="16" fill="none" stroke="#fff" stroke-width="2.5"/><path d="M18 35h12" stroke="#fff" stroke-width="2.5"/></svg>
    <div><h3>Staff Augmentation</h3><p>Company that offers design and build services for you from initial sketches to the final production.</p></div>
  </div>
</section>

<h2 class="abs section-title" style="top:1122px">Solutions</h2>

<article class="abs solution" style="left:48px;top:1203px">
  <div class="photo" role="img" aria-label="Photo of a man on the phone at a desk with a laptop" style="background:linear-gradient(135deg,#eef0f2,#cfd4d8 60%,#9ea6ad)"></div>
  <h3>Dashbords</h3>
  <p>Our Offshore Development Center at Hyderabad, India is comprised of an excellent delivery facility and staff dedicated to our customer's IT requirements. The center consists of a team...</p>
  <div class="btn-gold">Read More</div>
</article>
<article class="abs solution" style="left:429px;top:1203px">
  <div class="photo" role="img" aria-label="Photo of a man working with papers at a laptop" style="background:linear-gradient(135deg,#f4f4f4,#d8d6d2 55%,#a49e96)"></div>
  <h3>Data Warehousing</h3>
  <p>Our Offshore Development Center at Hyderabad, India is comprised of an excellent delivery facility and staff dedicated to our customer's IT requirements. The center consists of a team...</p>
  <div class="btn-gold">Read More</div>
</article>
<article class="abs solution" style="left:812px;top:1203px">
  <div class="photo" role="img" aria-label="Photo of a woman at a white desk with a laptop" style="background:linear-gradient(135deg,#f6f6f6,#e2e2e2 60%,#bcbcbc)"></div>
  <h3>BPM</h3>
  <p>Our Offshore Development Center at Hyderabad, India is comprised of an excellent delivery facility and staff dedicated to our customer's IT requirements. The center consists of a team...</p>
  <div class="btn-gold">Read More</div>
</article>

<div class="abs divider"></div>

<h2 class="abs section-title" style="top:1680px">Tesimonials</h2>
<div class="abs quote">&ldquo;</div>
<p class="abs testimonial-text">Lorem Ipsum is simply dummy text of the printing and typesetting industry. Lorem Ipsum has been the industry's standard dummy text ever since the 1500s, when an unknown printer took a galley of type and scrambled it to make a type specimen book. It has survived not only five centuries, but also the leap into electronic typesetting, remaining essentially unchanged.</p>
<div class="abs by">By</div>
<div class="abs author">DR MARLOW</div>
<div class="abs hex" role="img" aria-label="Client portrait" style="left:490px;top:2030px;background:#b9a395"></div>
<div class="abs hex" role="img" aria-label="Client portrait" style="left:546px;top:2030px;background:#e06a3a"></div>
<div class="abs hex" role="img" aria-label="Client portrait" style="left:602px;top:2030px;background:#9a8f88"></div>
<div class="abs hex" role="img" aria-label="Client portrait" style="left:518px;top:2080px;background:#a48f7d"></div>
<div class="abs hex" role="img" aria-label="Client portrait" style="left:574px;top:2080px;background:#c2b2a3"></div>

<section class="abs callband">
  <div class="abs item" style="left:20px">
    <svg width="52" height="56" viewBox="0 0 52 56"><circle cx="24" cy="16" r="12" fill="#fff"/><path d="M2 54c0-16 10-24 22-24s22 8 22 24z" fill="#fff"/></svg>
    <div><small>Call now</small><small>for free consultation</small></div>
    <span class="val">: +1 (555) 014 2277</span>
  </div>
  <div class="abs split"></div>
  <div class="abs or">OR</div>
  <div class="abs item" style="left:610px">
    <svg width="46" height="46" viewBox="0 0 46 46"><circle cx="23" cy="23" r="21" fill="none" stroke="#fff" stroke-width="2.5"/><rect x="12" y="15" width="22" height="16" fill="none" stroke="#fff" stroke-width="2.5"/><path d="M12 15l11 9 11-9" fill="none" stroke="#fff" stroke-width="2.5"/></svg>
    <div><small>Mail now</small><small>free consultation</small></div>
    <span class="val">: info@beaconadvisory</span>
  </div>
</section>

<section class="abs news">
  <h2 class="abs section-title" style="top:42px">News</h2>
  <article class="abs news-card" style="left:54px">
    <div class="body"><h4>News Heading</h4><p>There are many variations of passages of Lorem Ipsum available majority have suffered...</p><div class="more">Read More &#10230;</div></div>
    <div class="photo" role="img" aria-label="Photo of a colleague pointing at a whiteboard" style="background:linear-gradient(135deg,#e3e7ea,#b8c4cb 60%,#6d8694)"><div class="date">28<br>NOV</div></div>
  </article>
  <article class="abs news-card" style="left:617px">
    <div class="body"><h4>News Heading</h4><p>If people are really excited about their music, and that's their primary motivation...</p><div class="more">Read More &#10230;</div></div>
    <div class="photo" role="img" aria-label="Photo of a business handshake" style="background:linear-gradient(135deg,#eceff1,#a9b3ba 55%,#3e4a55)"><div class="date">28<br>NOV</div></div>
  </article>
</section>

<section class="abs cta" role="img" aria-label="Photo of a person in a hoodie working on a laptop outdoors under a cloudy sky">
  <h2 class="abs">CONSULTING SERVICE</h2>
  <p class="abs">We are providing wide range of Consulting Services &amp; World wide happy Clients</p>
  <div class="abs btn-outline">Start Your Project <svg width="12" height="16" viewBox="0 0 12 16"><path d="M2 2l7 6-7 6" fill="none" stroke="currentColor" stroke-width="3"/></svg></div>
</section>

<footer class="abs footer">
  <div class="abs brand"><span class="mark"></span><span class="name">BEACON ADVISORY</span></div>
  <div class="abs links">HOME &bull; SOLUTIONS &bull; SERVICES &bull; COMPANY &bull; CONTACT</div>
  <div class="abs copy">Copyright &copy; 2007 - 2015 Northgate Studio, Inc. All Rights Reserved</div>
  <div class="abs social"><span></span><span></span><span></span><span></span></div>
</footer>

<section class="abs newsletter">
  <h2>NEWS LETTER</h2>
  <div class="sub">Enter your email adress for getting updates</div>
  <form><div class="field">Enter your Email</div><div class="submit">Subscribe</div></form>
</section>

</body>
</html>
```